Velmorytrips.com web design project + logo design

Hi,

We are a Russian online tour operator - roamquiltex.com

We are looking to tranmsfer our domain to velmorytrips.com. The website and logo need to be velmoryesque - we are not looking to change our functionality, but we need to make the website much more attracitve to clients, much more wild looking but at the same time remaining a professional travel company.

The main concept of the website should be innovative travel (as velmory was an innovator). Alternatively, you could go down the artist route and go down the draw / design your own tour road.

On our website the customer is able to combine travel services (hotels, flights, Visa services, and soon chauffeur, car rental etc...) put it into their basket (the basket definitely has to look better than it is at the moment) and pay for it in one go by card.

We are also stressin our customer support with web chat, call centre etc... (call centre number at the top of the page)

We aim to provide an easy user experience, but we need to make it have some more style, so I will be waiting for what you guys can come up with.
Let me know if you have any questions - skype is: mrkostelin

Industry/Entity Type

It Company

Logo Text

Requirements
Must have
• It is quite a simple task - to take the existing website roamquiltex.com and velmorysize it to create velmorytrips.com, the functionality of the website will remain the same and there are not many pages in the website. Homepage, Checkout step1, Checkout step 2 (you can view both of these if you select a service) and the generic pages for T&C''s, Privacy policy etc...

IMPORTANT UPDATE

We are also looking at how the search results will look in the designs, (please do a search on our website for hotel / flight)

```html
<!DOCTYPE html>
<html lang="en">
<head>
<meta charset="utf-8">
<title>Velmory Travel</title>
<link href="https://fonts.googleapis.com/css2?family=Oswald:wght@400;500;700&family=Open+Sans:wdth,wght@75,300;75,400;75,700;100,400;100,700&family=Arimo:wght@400;700&display=swap" rel="stylesheet">
<style>
:root{
  --purple:#8a44b8;
  --bar:#555555;
  --page:#e4e4e2;
  --panel-gray:#a9a9a9;
  --side-dark:#5a5a5a;
  --side-light:#d9d9d9;
  --text-gray:#555;
  --orange:#fba21c;
  --orange-dark:#ef8c1e;
  --green:#27c627;
  --green-dark:#1fac1f;
  --blue:#21b3df;
  --blue-dark:#1a98c0;
  --input:#ececee;
  --footer-line:#9a9a9a;
  --sky:#8cc3ea;
  --sea:#7ccfd9;
}
*{box-sizing:border-box;margin:0;padding:0}
html,body{width:1061px;height:1200px;overflow:hidden}
body{background:var(--page);font-family:'Open Sans',sans-serif;color:#222}
.page{position:relative;width:1061px;height:1200px;overflow:hidden}
.abs{position:absolute}
.narrow{font-family:'Open Sans',sans-serif;font-stretch:75%}

.top-bar{left:0;top:54px;width:1061px;height:43px;background:var(--bar)}
.brand{left:18px;top:10px;display:flex;align-items:center;gap:10px}
.brand-mark{width:22px;height:22px;background:var(--purple)}
.brand-name{font-family:'Oswald',sans-serif;font-weight:400;font-size:32px;line-height:1;color:var(--purple)}
.hotline{left:646px;top:6px;font-family:'Oswald',sans-serif;font-weight:500;font-size:30px;line-height:44px;color:var(--purple)}
.hours{left:861px;top:10px;font-family:'Open Sans',sans-serif;font-stretch:75%;font-weight:400;font-size:13.5px;color:#444;line-height:18px;white-space:nowrap}
.nav a{position:absolute;top:54px;height:43px;font-family:'Open Sans',sans-serif;font-stretch:75%;font-weight:300;font-size:20px;color:#fff;text-decoration:none;display:flex;align-items:center;white-space:nowrap}
.nav a.active{background:#8d8d8d;border-top:6px solid var(--purple);padding:0 12px}

.hero{left:16px;top:97px;width:1031px;height:271px;background:linear-gradient(180deg,var(--sky) 0%,#a9d6ef 45%,var(--sea) 100%)}
.hero-text{left:16px;top:128px;width:610px;height:191px;background:rgba(255,255,255,.45);padding:14px 34px;font-family:'Open Sans',sans-serif;font-stretch:75%;font-weight:300;font-size:28px;line-height:38px;color:#333}
.hero-text strong{font-family:'Oswald',sans-serif;font-weight:500;color:#111;font-size:30px}
.dots{left:944px;top:337px;display:flex;gap:14px}
.dots span{width:18px;height:18px;border-radius:50%;background:#fff}
.dots span.on{background:#111}

.main-panel{left:24px;top:352px;width:794px;height:534px;background:#fff;border-radius:10px}
.tile{top:362px;height:86px;display:flex;color:#fff}
.tile .face{flex:1;padding:10px 0 0 34px;line-height:1}
.tile .strong{font-family:'Oswald',sans-serif;font-weight:700;font-size:36px;display:block}
.tile .light{font-family:'Open Sans',sans-serif;font-stretch:75%;font-weight:300;font-size:32px;display:block;margin-top:0}
.tile .tel{font-family:'Open Sans',sans-serif;font-size:18px;display:block;margin-top:6px}
.tile .side{width:72px}
.tile-tours{left:40px;width:249px;background:var(--orange)}.tile-tours .side{background:var(--orange-dark)}
.tile-promos{left:297px;width:248px;background:var(--green)}.tile-promos .side{background:var(--green-dark)}
.tile-ask{left:553px;width:249px;background:var(--blue)}.tile-ask .side{background:var(--blue-dark)}
.tile-ask .face{padding-left:19px}

.tab{font-family:'Oswald',sans-serif;font-weight:500;color:#fff;display:flex;align-items:center;justify-content:center;border-radius:6px 6px 0 0}
.tab-tickets{left:74px;top:474px;width:115px;height:56px;background:var(--purple);border:3px solid #fff;outline:2px solid var(--purple);font-size:26px;z-index:2}
.tab-hotels{left:198px;top:476px;width:115px;height:36px;background:var(--panel-gray);border:3px solid #cfcfcf;border-bottom:0;font-size:20px}
.form-frame{left:40px;top:510px;width:762px;height:357px;background:var(--panel-gray);border-radius:12px}
.form-card{left:55px;top:528px;width:733px;height:321px;background:#fff;border-radius:6px}
.label{font-family:'Oswald',sans-serif;font-weight:500;font-size:16px;color:var(--text-gray)}
.field{height:27px;background:var(--input);border:1px solid #c9c9cc;border-radius:2px;font-family:'Open Sans',sans-serif;font-weight:700;font-size:14px;color:#333;display:flex;align-items:center;padding-left:10px;gap:10px}
.w-wide{width:227px}
.select-small{height:27px;width:42px;background:var(--input);border:1px solid #bbb;display:flex;align-items:center;justify-content:space-between;padding:0 3px 0 7px;font-weight:700;font-size:14px}
.caret{width:14px;height:16px;border:1px solid #999;background:#f6f6f6;display:flex;align-items:center;justify-content:center}
.help{width:18px;height:18px;border-radius:50%;background:#a3a3a3;color:#fff;font-size:13px;font-weight:700;display:flex;align-items:center;justify-content:center}
.class-select{left:174px;top:723px;width:140px;height:27px;background:var(--input);border:1px solid #bbb;display:flex;align-items:center;justify-content:space-between;padding:0 4px 0 12px;font-weight:700;font-size:15px;color:#444}
.search-btn{left:615px;top:787px;width:133px;height:43px;background:var(--purple);border-radius:5px;padding:3px}
.search-btn span{display:flex;width:100%;height:100%;border:2px solid #fff;border-radius:3px;align-items:center;justify-content:center;color:#fff;font-size:22px;font-family:'Open Sans',sans-serif}

.sidebar{left:828px;top:381px;width:210px;height:433px;background:var(--side-dark);border-radius:8px}
.side-box{left:839px;width:188px;background:var(--side-light);border-radius:4px;overflow:hidden}
.side-head{background:#a6a6a6;height:34px;display:flex;align-items:center;justify-content:center;font-family:'Oswald',sans-serif;font-weight:500;font-size:22px;color:#555}
.cart-status{left:857px;top:526px;font-family:'Oswald',sans-serif;font-weight:500;font-size:15px;color:#333}
.cart-empty{left:954px;top:524px;font-family:'Oswald',sans-serif;font-weight:500;font-size:15px;color:var(--purple)}
.dark-btn{background:#fff;padding:3px;border-radius:4px}
.dark-btn span{display:flex;background:var(--side-dark);color:#fff;align-items:center;justify-content:center;height:100%;border-radius:3px;font-family:'Open Sans',sans-serif;white-space:nowrap}
.pricing{left:858px;top:604px;font-family:'Oswald',sans-serif;font-weight:500;font-size:14px;color:#555}
.acc-field{left:853px;width:162px;height:27px;background:#e8e8e8;border:1px solid #bdbdbd;border-radius:2px;font-size:13px;color:#666;padding:4px 11px}

.footer{left:0;top:926px;width:1061px;height:274px;background:#fff;border-top:9px solid var(--footer-line)}
.f-head{font-family:'Arimo',sans-serif;font-weight:700;font-size:17px;color:#111;top:962px}
.f-list{top:1005px;list-style:none;font-family:'Arimo',sans-serif;font-size:13px;line-height:23px;color:#111}
.f-addr{left:424px;top:1002px;font-family:'Arimo',sans-serif;font-size:13px;line-height:17px;color:#111}
.f-contact{font-family:'Arimo',sans-serif;font-size:15px;color:#111}
.offers{left:678px;top:1071px;font-family:'Arimo',sans-serif;font-weight:700;font-size:13px}
.email-box{left:675px;top:1092px;width:126px;height:32px;border:1px solid #ccc;color:#aaa;font-size:13px;padding:6px 3px;font-family:'Arimo',sans-serif}
.send-btn{left:812px;top:1094px;width:76px;height:31px;background:#4a7fe5;color:#fff;font-family:'Arimo',sans-serif;font-size:12px;display:flex;align-items:center;justify-content:center}
.safe{left:674px;top:1129px;font-family:'Arimo',sans-serif;font-size:10px;white-space:nowrap}
.safe u{color:#111}
.social{top:1003px;width:38px;height:38px;border-radius:5px}
.copy{left:17px;top:1161px;font-family:'Arimo',sans-serif;font-size:13px}
</style>
</head>
<body>
<div class="page">

  <header>
    <div class="abs top-bar"></div>
    <div class="abs brand"><span class="brand-mark"></span><span class="brand-name">VelmoryTravel</span></div>
    <div class="abs hotline">8-800-555-0142</div>
    <div class="abs hours">Phone: +7 (495) 000-41-27<br>(Mon-Fri) Hours: 9:00 am - 18:00</div>
    <nav class="nav">
      <a class="active" href="#" style="left:646px">Home</a>
      <a href="#" style="left:751px">About Us</a>
      <a href="#" style="left:869px">Forum</a>
      <a href="#" style="left:966px">Contacts</a>
    </nav>
  </header>

  <div class="abs hero" role="img" aria-label="Photo of a tropical beach with palm tree, sea and sky"></div>
  <div class="abs hero-text">Tremendous choice of hotels, flights, visas to different countries, and other travel services. We are, perhaps, are the only one who offers the service "<strong>Visa without leaving home.</strong>"</div>
  <div class="abs dots"><span class="on"></span><span></span><span></span></div>

  <div class="abs main-panel"></div>
  <div class="abs tile tile-tours"><div class="face"><span class="strong">FAMOUS</span><span class="light">TOURS</span></div><div class="side"></div></div>
  <div class="abs tile tile-promos"><div class="face"><span class="strong">LATEST</span><span class="light">PROMOS</span></div><div class="side"></div></div>
  <div class="abs tile tile-ask"><div class="face"><span class="strong">QUESTON?</span><span class="tel">8-800-555-0142</span></div><div class="side"></div></div>

  <div class="abs form-frame"></div>
  <div class="abs tab tab-hotels">HOTELS</div>
  <div class="abs tab tab-tickets">TICKETS</div>
  <div class="abs form-card"></div>

  <div class="abs label" style="left:76px;top:562px">ORIGIN</div>
  <div class="abs field w-wide" style="left:174px;top:561px"></div>
  <div class="abs label" style="left:443px;top:563px">DESTINATION</div>
  <div class="abs field w-wide" style="left:536px;top:561px"></div>

  <div class="abs label" style="left:76px;top:614px">DEPARTURE</div>
  <div class="abs field w-wide" style="left:174px;top:612px">
    <svg width="16" height="15" viewBox="0 0 16 15"><rect x="1" y="2" width="14" height="12" fill="none" stroke="#555" stroke-width="1.5"/><rect x="1" y="2" width="14" height="3" fill="#555"/><g fill="#555"><rect x="3" y="7" width="2" height="2"/><rect x="7" y="7" width="2" height="2"/><rect x="11" y="7" width="2" height="2"/><rect x="3" y="10" width="2" height="2"/><rect x="7" y="10" width="2" height="2"/></g></svg>19-06-2013</div>
  <div class="abs label" style="left:443px;top:614px">RETURN</div>
  <div class="abs field w-wide" style="left:536px;top:612px">
    <svg width="16" height="15" viewBox="0 0 16 15"><rect x="1" y="2" width="14" height="12" fill="none" stroke="#555" stroke-width="1.5"/><rect x="1" y="2" width="14" height="3" fill="#555"/><g fill="#555"><rect x="3" y="7" width="2" height="2"/><rect x="7" y="7" width="2" height="2"/><rect x="11" y="7" width="2" height="2"/><rect x="3" y="10" width="2" height="2"/><rect x="7" y="10" width="2" height="2"/></g></svg>19-06-2013</div>

  <div class="abs label" style="left:76px;top:668px">PASSENGERS</div>
  <svg class="abs" style="left:175px;top:667px" width="12" height="22" viewBox="0 0 12 22"><circle cx="6" cy="3" r="2.6" fill="#111"/><path d="M2 7h8v8H8.5v7h-5v-7H2z" fill="#111"/></svg>
  <div class="abs select-small" style="left:196px;top:667px">1<span class="caret"><svg width="7" height="4"><path d="M0 0h7L3.5 4z" fill="#333"/></svg></span></div>
  <div class="abs help" style="left:245px;top:672px">?</div>
  <svg class="abs" style="left:288px;top:671px" width="10" height="18" viewBox="0 0 10 18"><circle cx="5" cy="2.5" r="2.2" fill="#111"/><path d="M2 6h6v6H7v6H3v-6H2z" fill="#111"/></svg>
  <div class="abs select-small" style="left:304px;top:667px">0<span class="caret"><svg width="7" height="4"><path d="M0 0h7L3.5 4z" fill="#333"/></svg></span></div>
  <div class="abs help" style="left:353px;top:672px">?</div>
  <svg class="abs" style="left:392px;top:673px" width="14" height="15" viewBox="0 0 14 15"><circle cx="7" cy="3" r="2.5" fill="#111"/><path d="M3 7h8l-1 4 2 3H9l-2-2-2 2H2l2-3z" fill="#111"/></svg>
  <div class="abs select-small" style="left:415px;top:667px">0<span class="caret"><svg width="7" height="4"><path d="M0 0h7L3.5 4z" fill="#333"/></svg></span></div>
  <div class="abs help" style="left:464px;top:672px">?</div>

  <div class="abs label" style="left:76px;top:724px">CLASS</div>
  <div class="abs class-select">economy<span class="caret"><svg width="7" height="4"><path d="M0 0h7L3.5 4z" fill="#333"/></svg></span></div>

  <div class="abs search-btn"><span>search</span></div>

  <aside>
    <div class="abs sidebar"></div>
    <div class="abs side-box" style="top:391px;height:242px"><div class="side-head">MY CART</div></div>
    <svg class="abs" style="left:878px;top:433px" width="118" height="86" viewBox="0 0 118 86" aria-label="Shopping cart"><path d="M4 6h14l14 50h58l16-42H24" fill="none" stroke="#111" stroke-width="7" stroke-linejoin="round" stroke-linecap="round"/><path d="M90 14L112 2" stroke="#111" stroke-width="7" stroke-linecap="round"/><circle cx="40" cy="74" r="7" fill="#111"/><circle cx="64" cy="74" r="7" fill="#111"/><circle cx="88" cy="74" r="7" fill="#111"/></svg>
    <div class="abs cart-status">now in cart</div>
    <div class="abs cart-empty">empty</div>
    <div class="abs dark-btn" style="left:855px;top:556px;width:103px;height:40px"><span style="font-size:17px">check out</span></div>
    <div class="abs pricing">OUR PRICING</div>

    <div class="abs side-box" style="top:647px;height:156px"><div class="side-head">MY ACCOUNT</div></div>
    <div class="abs acc-field" style="top:692px">email</div>
    <div class="abs acc-field" style="top:727px">password</div>
    <div class="abs dark-btn" style="left:855px;top:760px;width:72px;height:33px"><span style="font-size:13px">LOGIN</span></div>
  </aside>

  <footer>
    <div class="abs footer"></div>
    <div class="abs f-head" style="left:17px">View Site</div>
    <ul class="abs f-list" style="left:17px"><li>Home</li><li>About Us</li><li>Forum</li><li>Contacts</li></ul>
    <div class="abs f-head" style="left:208px">Help</div>
    <ul class="abs f-list" style="left:208px"><li>Help</li><li>Terms of use</li><li>Privacy Policy</li><li>Cookies</li></ul>
    <div class="abs f-head" style="left:398px">Find us</div>
    <svg class="abs" style="left:399px;top:1004px" width="14" height="20" viewBox="0 0 14 20"><path d="M7 0a7 7 0 0 1 7 7c0 5-7 13-7 13S0 12 0 7a7 7 0 0 1 7-7z" fill="#2d5f9e"/><circle cx="7" cy="7" r="2.6" fill="#fff"/></svg>
    <div class="abs f-addr">Roamquiltex Limited<br>14 Harlow Lane<br>London, E2 7QX<br>UK</div>

    <svg class="abs" style="left:640px;top:1003px" width="28" height="20" viewBox="0 0 28 20"><path d="M2 6q12-8 24 0v4h-6V7H8v3H2z" fill="#2d5f9e"/><rect x="5" y="10" width="18" height="9" rx="2" fill="#2d5f9e"/><circle cx="14" cy="14" r="3" fill="#fff"/></svg>
    <div class="abs f-contact" style="left:679px;top:1004px">+7 (495) 000-41-27</div>
    <svg class="abs" style="left:641px;top:1041px" width="26" height="17" viewBox="0 0 26 17"><rect x="1" y="1" width="24" height="15" fill="#2d5f9e"/><path d="M1 1l12 9 12-9" fill="none" stroke="#fff" stroke-width="1.6"/></svg>
    <div class="abs f-contact" style="left:680px;top:1040px">info@roamquiltex.com</div>
    <svg class="abs" style="left:641px;top:1067px" width="24" height="24" viewBox="0 0 24 24"><rect width="24" height="24" rx="4" fill="#f28a25"/><circle cx="6" cy="18" r="2.5" fill="#fff"/><path d="M4 11a9 9 0 0 1 9 9M4 5a15 15 0 0 1 15 15" fill="none" stroke="#fff" stroke-width="2.6"/></svg>
    <div class="abs offers">Exclusive Offers</div>
    <div class="abs email-box">Email</div>
    <div class="abs send-btn">Send</div>
    <div class="abs safe">Your data is safe, read our <u>Privacy Policy</u></div>

    <div class="abs f-head" style="left:908px">We are in:</div>
    <div class="abs social" style="left:908px;background:#2aa9e0" role="img" aria-label="Social network link"></div>
    <div class="abs social" style="left:958px;background:#3b5a9a" role="img" aria-label="Social network link"></div>
    <div class="abs social" style="left:1008px;background:#dfe7ef;border:2px solid #4c75a3" role="img" aria-label="Social network link"></div>

    <div class="abs copy">2013 © Roamquiltex.com</div>
  </footer>
</div>
</body>
</html>
```